Business Card design for a mobile solutions company

- we are a mobile telecommunications company focusing on mobile content and solutions
- we are based in Malaysia however operate a regional business
- attached is our company logo and current business card design
- please try to incorporate the "cubes" into the design

our company philosophy is dynamic and outgoing. we are a lean team of less than 50, but we have strong roots in the mobile industry in Asia and we like to challenge ourselves by taking on larger projects.

we love joint ventures and working with partners to find the right solutions for our clients

*please feel free to modify our logo (typeface etc)
**we would like to keep the 3 cube design for the logo, but I would love to see different versions of it

some of the designs are great and I think our logo (especially the typeface used for the words) doesn't look good. please feel free to update the logo but try to keep the cubes, you are free to modify the cubes and update them.

Reason: looking for more design please

Industry/Entity Type

Telecommunications

Font styles to use
Sans Serif

```html
<!DOCTYPE html>
<html lang="en">
<head>
<meta charset="utf-8">
<title>Vantor Mobile – Business Card</title>
<link rel="stylesheet" href="https://fonts.googleapis.com/css2?family=Open+Sans:ital,wght@0,400;0,600;0,700;1,400&display=swap">
<style>
  :root {
    --bg-top: #b9b9b9;
    --bg-bottom: #8e8e8e;
    --card: #0b0b0b;
    --card-edge: rgba(70, 70, 70, 0.9);
    --texture-light: #2a2a2a;
    --texture-dark: #050505;
    --ink: #ffffff;
    --ink-soft: #e6e6e6;
    --accent-square: #3a86cf;
  }
  * { margin: 0; padding: 0; box-sizing: border-box; }
  html, body { width: 1147px; height: 1200px; overflow: hidden; }
  body {
    background: linear-gradient(180deg, var(--bg-top), var(--bg-bottom));
    font-family: "Open Sans", Arial, sans-serif;
    color: var(--ink);
    position: relative;
  }
  .card {
    position: absolute;
    left: 261px;
    width: 592px;
    height: 346px;
    border-radius: 20px;
    background: var(--card);
    border: 7px solid var(--card-edge);
    overflow: hidden;
  }
  .card--front { top: 227px; }
  .card--back { top: 626px; }
  .card__texture {
    position: absolute;
    inset: 0;
    background: linear-gradient(175deg, var(--texture-light) 0%, #141414 45%, var(--texture-dark) 80%);
  }
  .brand {
    position: absolute;
    display: flex;
    align-items: center;
    gap: 12px;
    font-weight: 600;
    letter-spacing: 0.2px;
    white-space: nowrap;
  }
  .brand__mark { background: var(--accent-square); flex: none; }
  .card--front .brand { left: 20px; top: 88px; font-size: 27px; flex-direction: column; align-items: flex-start; gap: 14px; }
  .card--front .brand__mark { width: 44px; height: 44px; }
  .card--back .brand { left: 0; right: 0; top: 22px; justify-content: center; flex-direction: column; gap: 16px; font-size: 44px; }
  .card--back .brand__mark { width: 80px; height: 80px; }
  .contact {
    position: absolute;
    right: 16px;
    top: 150px;
    width: 210px;
    text-align: right;
  }
  .contact__name { font-size: 19px; font-weight: 600; line-height: 1.2; }
  .contact__role {
    font-size: 15px; font-style: italic; line-height: 1.4;
    padding-bottom: 6px;
    border-bottom: 1.5px solid var(--ink-soft);
  }
  .contact__list { list-style: none; margin-top: 10px; font-size: 11.5px; color: var(--ink-soft); }
  .contact__list li { display: flex; justify-content: flex-end; align-items: center; gap: 5px; height: 23px; }
  .contact__list svg { width: 11px; height: 11px; fill: var(--ink-soft); }
  .address {
    position: absolute;
    left: 0; right: 0; top: 262px;
    text-align: center;
    font-size: 11.5px;
    line-height: 17px;
    color: var(--ink-soft);
  }
</style>
</head>
<body>
  <section class="card card--front">
    <div class="card__texture" role="img" aria-label="Dark field of glossy black cubes receding into the distance"></div>
    <div class="brand"><span class="brand__mark"></span>VANTOR MOBILE</div>
    <div class="contact">
      <p class="contact__name">Adrian Koh</p>
      <p class="contact__role">Chief Marketing Officer</p>
      <ul class="contact__list">
        <li>+60 3 555 0182
          <svg viewBox="0 0 12 12"><path d="M1 4c0-2 2-3 5-3s5 1 5 3v1H8.5V3.8H3.5V5H1zM2.5 6.5h7L11 11H1z"/></svg></li>
        <li>+ 62 855 0007261
          <svg viewBox="0 0 12 12"><rect x="0" y="0" width="12" height="12" rx="2"/><path d="M4 2.5l1.5 2-1 1c.6 1.2 1.3 1.9 2.5 2.5l1-1 2 1.5-1 1.5C6 9.5 2.5 6 2.5 3.5z" fill="#0b0b0b"/></svg></li>
        <li>adrian@vantormobile.com.my
          <svg viewBox="0 0 12 12"><path d="M0 2h12v8H0z"/><path d="M0 2l6 4.5L12 2" fill="none" stroke="#0b0b0b" stroke-width="1"/></svg></li>
      </ul>
    </div>
  </section>

  <section class="card card--back">
    <div class="card__texture" role="img" aria-label="Dark field of glossy black cubes receding into the distance"></div>
    <div class="brand"><span class="brand__mark"></span>VANTOR MOBILE</div>
    <address class="address" style="font-style:normal">
      Vantor Mobile SDN BHD<br>
      Unit 5-1, Level 5 Block 2 Menara Seri, Damai Park No.12,<br>
      Jalan Cempaka, 59100 Kuala Lumpur
    </address>
  </section>
</body>
</html>
```